Business Cards and Stationery - Real Estate
See "information" and "additional comments"
Business Cards and Stationery - Real Estate - Real Estate
Creative Brief
Professional
Anselm Varga
Managing Broker
4382 SW Route 14, Ste 305 Vancouver, WA 98671
Direct - 360-555-0147
Cell - 360-555-0193
anselm@fernloftpm.example
www.fernlofthomes.example
Licensed in OR & WA
We want to use UV spotting on our cards. Here is a video link from the printing company we are using. If you are unfamiliar with creating files for UV spotting, it requires one file for the card and a second mask file for the UV spotting. https://www.clipvault.example/watch?v=Qx7rLm2PzA1 I've uploaded the template files to use from Zentra Print along with our Adobe Illustrator Logo files and a head shot. We probably don't want a head shot on the card, but have uploaded just in case. Please use Adobe Illustrator.
Probably just the logo. Something that is clean, possible a repeated design such as the logo. Would like to consider UV spotting on back. Try searching for "business cards spot uv" on Google, then look at the "images" link.
SiteAdmin SiteAdmin
Dear Designers, Kindly follow the below mention instructions by the Project holder for better and improve designs: We want to use spot UV on our cards, front and back. Here is a video Link from the printing company we are using. If you are unfamiliar with creating file for Spot UV, it requires one file for the card and a second mask file for the UV spotting. https://www.clipvault.example/watch?v=Qx7rLm2PzA1 Use your creativity, but a couple ideas for the back would be to repeat our logo over and over across the entire back. It may be nice to somehow put our website within those repeated logos. Or it may not be nice, depending on how it looks. You could also just make our logo with URL on the back. For the front, you will have to be creative to make it work. Our logo could be UV spotted. And then probably some sort of nice design that covers a portion of the front, keeping in mind that the uv spot coating design can overlap anything. Or maybe it would look best to only spot uv our logo. The content for the card is in our creative brief. We would also like to include "We Love Referrals!" somewhere on the card. Here are a few images for some ideas. Keep in mind that we don't want a copy of what is done with these ideas. They are simply ideas of what can be done with UV spotting. https://pressglow.example/assets/images/gallery/business-cards/images/a1b2c3d4e5f60718293a4b5c6d7e8f90.png https://pressglow.example/assets/uploads/spot_uv_marlow_business_cards.jpg http://media.shopweave.example/51730264/Renata-Pell-spot-gloss-silver-foil-spot-uv-silk-unique-cool-business-cards_full.jpeg http://www.quartzlinecards.example/images/img-gallery/silk-business-card-with-spot-uv-harrow-cellars.jpg http://i01.i.tradepix.example/wsphoto/v2/813406572_2/Custom-Spot-UV-business-card-matt-coated-paper-350gsm-High-quality.jpg http://www.newswire.example/64028195-silk-laminated-business-cards-with-spot-uv.jpg http://www.atelier-cartes-nord.example/wp-content/uploads/2010/10/carte-commerciale-vernis-selectif.jpg https://pressglow.example/assets/uploads/spot_uv_cards_dravetek.jpg http://www.calloutmailers.example/wp/wp-content/uploads/2013/03/zebra-orange-spot-uv-business-card1.png http://layoutharbor.example/wp-content/uploads/2013/04/square-business-card-29.jpg
fernloft47 fernloft47
I forgot to add on that last comment, that the black designs are way to dark for our tastes. Blue on the back looks nice. We prefer the lighter designs on the front of the card.
We are looking for double sided cards with rounded corners and some UV spotting on both sides. We like the design of #96 on the back side, however it looks like there may be some silver foil on the logo. We won't be doing foil, just spotting. There are a lot of nice designs so far, but we need to have the combination of rounded corners and UV spotting. Thanks.

```html
<!DOCTYPE html>
<html lang="en">
<head>
<meta charset="utf-8">
<title>Fernloft Homes – Stationery Set</title>
<link href="https://fonts.googleapis.com/css2?family=Montserrat:wght@400;600;800&display=swap" rel="stylesheet">
<style>
  :root {
    --brand-blue: #1f4d8c;
    --brand-gray: #6d7076;
    --ink: #3a3c40;
    --muted: #8a8d92;
    --paper: #ffffff;
    --backdrop: #efefef;
  }
  * { box-sizing: border-box; margin: 0; padding: 0; }
  html, body { width: 1200px; height: 936px; overflow: hidden; }
  body {
    background: var(--backdrop);
    font-family: "Montserrat", sans-serif;
    color: var(--ink);
    position: relative;
  }
  .sheet {
    position: absolute;
    background: var(--paper);
    box-shadow: 0 2px 6px rgba(0,0,0,0.12);
    overflow: hidden;
  }
  .brand { display: flex; align-items: center; gap: 6px; }
  .brand-square { background: var(--brand-blue); flex: none; }
  .brand-name { color: var(--brand-blue); font-weight: 800; letter-spacing: 0.04em; white-space: nowrap; }
  .footer-band { position: absolute; left: 0; bottom: 0; width: 100%; }
  .footer-url { position: absolute; color: #fff; font-weight: 600; }

  /* Letterhead */
  .letterhead { left: 183px; top: 76px; width: 388px; height: 558px; }
  .letterhead .brand { position: absolute; left: 26px; top: 28px; }
  .letterhead .brand-square { width: 16px; height: 16px; }
  .letterhead .brand-name { font-size: 11px; }
  .letterhead .contact { position: absolute; right: 26px; top: 28px; text-align: right; font-size: 5px; line-height: 1.6; color: var(--muted); }
  .letter-body { position: absolute; left: 38px; top: 100px; width: 312px; font-size: 5px; line-height: 1.7; color: var(--muted); }
  .letter-body p { margin-bottom: 8px; }
  .letter-body .sign-name { margin-top: 26px; color: var(--ink); font-weight: 600; }
  .letterhead .footer-url { left: 12px; bottom: 4px; font-size: 5px; }

  /* Folder */
  .folder { left: 634px; top: 76px; width: 368px; height: 546px; }
  .folder .brand { position: absolute; left: 50%; top: 228px; transform: translateX(-50%); flex-direction: column; gap: 14px; }
  .folder .brand-square { width: 60px; height: 60px; }
  .folder .brand-name { font-size: 24px; }
  .folder .footer-url { left: 14px; bottom: 7px; font-size: 6px; }

  /* Business cards */
  .card { width: 208px; height: 104px; border-radius: 5px; }
  .card-front { left: 46px; top: 665px; }
  .card-front .brand { position: absolute; left: 12px; top: 14px; gap: 4px; }
  .card-front .brand-square { width: 10px; height: 10px; }
  .card-front .brand-name { font-size: 7px; }
  .card-front .person { position: absolute; left: 12px; top: 34px; font-size: 5px; line-height: 1.5; }
  .card-front .person strong { display: block; font-weight: 600; font-size: 6px; }
  .card-front .details { position: absolute; right: 10px; top: 34px; text-align: right; font-size: 4px; line-height: 1.6; color: var(--muted); width: 110px; }
  .card-front .referral { position: absolute; left: 12px; bottom: 12px; font-size: 5px; color: var(--brand-blue); font-weight: 600; }
  .card-back { left: 46px; top: 792px; height: 114px; }
  .card-back .brand { position: absolute; left: 50%; top: 36px; transform: translateX(-50%); flex-direction: column; gap: 5px; }
  .card-back .brand-square { width: 16px; height: 16px; }
  .card-back .brand-name { font-size: 8px; }

  /* Envelope front */
  .envelope-front { left: 266px; top: 665px; width: 432px; height: 236px; }
  .envelope-front .brand { position: absolute; left: 18px; top: 22px; }
  .envelope-front .brand-square { width: 14px; height: 14px; }
  .envelope-front .brand-name { font-size: 9px; }
  .envelope-front .return-address { position: absolute; left: 18px; top: 46px; font-size: 4.5px; line-height: 1.6; color: var(--muted); }
  .envelope-front .footer-url { left: 14px; bottom: 6px; font-size: 6px; }

  /* Envelope back */
  .envelope-back { left: 736px; top: 665px; width: 431px; height: 236px; }
  .envelope-back .flap { position: absolute; left: 0; top: 0; width: 100%; height: 100%; }
</style>
</head>
<body>

<section class="sheet letterhead">
  <div class="brand"><span class="brand-square"></span><span class="brand-name">FERNLOFT HOMES</span></div>
  <div class="contact">
    4382 SW Route 14, Ste 305<br>Vancouver, WA 98671<br>Direct 360-555-0147<br>Cell 360-555-0193<br>anselm@fernloftpm.example
  </div>
  <div class="letter-body">
    <p>July 2, 2024</p>
    <p>Dear Owner,</p>
    <p>Thank you for trusting our team with your property. We manage every detail of leasing, upkeep and owner reporting so that your home stays rented, cared for and earning. Our local brokers answer calls quickly and visit each home on a regular schedule.</p>
    <p>This season we are adding online statements and faster repair requests for all owners and tenants in the Vancouver area.</p>
    <p>Please reach out with any questions about your account, and remember that we always welcome referrals from friends and neighbours. We look forward to another good year together.</p>
    <p>Sincerely,</p>
    <p class="sign-name">Anselm Varga<br><span style="font-weight:400;color:var(--muted)">Managing Broker</span></p>
  </div>
  <svg class="footer-band" viewBox="0 0 388 16" height="16" preserveAspectRatio="none" aria-hidden="true">
    <path d="M0 2 H140 Q150 2 156 9 L162 16 H0 Z" fill="var(--brand-blue)"/>
    <rect x="156" y="10" width="232" height="3" fill="var(--brand-gray)"/>
  </svg>
  <span class="footer-url">www.fernlofthomes.example</span>
</section>

<section class="sheet folder">
  <div class="brand"><span class="brand-square"></span><span class="brand-name">FERNLOFT HOMES</span></div>
  <svg class="footer-band" viewBox="0 0 368 24" height="24" preserveAspectRatio="none" aria-hidden="true">
    <path d="M0 2 H104 Q116 2 122 12 L130 24 H0 Z" fill="var(--brand-blue)"/>
    <rect x="124" y="16" width="244" height="4" fill="var(--brand-gray)"/>
  </svg>
  <span class="footer-url">www.fernlofthomes.example</span>
</section>

<section class="sheet card card-front">
  <div class="brand"><span class="brand-square"></span><span class="brand-name">FERNLOFT HOMES</span></div>
  <div class="person"><strong>Anselm Varga</strong>Managing Broker</div>
  <div class="details">
    Direct - 360-555-0147<br>Cell - 360-555-0193<br>anselm@fernloftpm.example<br>www.fernlofthomes.example<br>4382 SW Route 14, Ste 305<br>Vancouver, WA 98671<br>Licensed in OR &amp; WA
  </div>
  <div class="referral">We Love Referrals!</div>
</section>

<section class="sheet card card-back">
  <div class="brand"><span class="brand-square"></span><span class="brand-name">FERNLOFT HOMES</span></div>
  <svg class="footer-band" viewBox="0 0 208 10" height="10" preserveAspectRatio="none" aria-hidden="true">
    <path d="M0 1 H70 Q76 1 80 6 L83 10 H0 Z" fill="var(--brand-blue)"/>
    <rect x="80" y="6" width="128" height="2" fill="var(--brand-gray)"/>
  </svg>
</section>

<section class="sheet envelope-front">
  <div class="brand"><span class="brand-square"></span><span class="brand-name">FERNLOFT HOMES</span></div>
  <div class="return-address">4382 SW Route 14, Ste 305<br>Vancouver, WA 98671</div>
  <svg class="footer-band" viewBox="0 0 432 22" height="22" preserveAspectRatio="none" aria-hidden="true">
    <path d="M0 2 H120 Q132 2 138 11 L145 22 H0 Z" fill="var(--brand-blue)"/>
    <rect x="140" y="14" width="292" height="4" fill="var(--brand-gray)"/>
  </svg>
  <span class="footer-url">www.fernlofthomes.example</span>
</section>

<section class="sheet envelope-back">
  <svg class="flap" viewBox="0 0 431 236" aria-hidden="true">
    <path d="M0 0 H431 V30 Q431 40 420 42 L230 70 Q215 72 200 70 L10 42 Q0 40 0 30 Z" fill="var(--brand-blue)"/>
    <text x="215.5" y="30" text-anchor="middle" fill="#fff" font-family="Montserrat, sans-serif" font-weight="600" font-size="9" letter-spacing="1">www.fernlofthomes.example</text>
  </svg>
</section>

</body>
</html>
```